Professional Business Cards

We need a nice looking, profession and modern business card for our new company. Our logo is attatched

Target Market(s)

Young Professionals

Industry/Entity Type

Financial

Contact Information for Business Card

FRONT

Morvane Tally Pty Ltd
Level 22, Halden Court, 48 Wirrapool St
Sydney NSW 2000
ABN : 57 304 918 226

Derek Wallis - Chief Operations Officer
P : 02 7153 2819
M: 0418 395 207
derek@morvanetally,com

BACK

- Cryptocurrency Exchange Services
- Cryptocurrency Mining Operations
- Cryptocurrency Investment Fund Offering

Font styles to use
Sans Serif

Colors
0255a3
9d9d9d

```html
<!DOCTYPE html>
<html lang="en">
<head>
<meta charset="utf-8">
<title>Morvane Tally Business Card</title>
<link href="https://fonts.googleapis.com/css2?family=Montserrat:wght@400;500;600;700&display=swap" rel="stylesheet">
<style>
  :root {
    --brand-blue: #0255a3;
    --brand-blue-light: #1f6bb8;
    --brand-grey: #9d9d9d;
    --band-grey: #7a7a7a;
    --text-grey: #555555;
    --card-white: #ffffff;
    --canvas-bg: #e4e4e4;
  }
  * { margin: 0; padding: 0; box-sizing: border-box; }
  html, body {
    width: 1200px; height: 1000px; overflow: hidden;
    background: var(--canvas-bg);
    font-family: "Montserrat", Arial, sans-serif;
  }
  .card {
    position: absolute; left: 270px; width: 661px; height: 378px;
    box-shadow: 0 3px 8px rgba(0,0,0,0.25);
    overflow: hidden;
  }
  /* Reverse side */
  .card-back {
    top: 108px;
    background: linear-gradient(120deg, var(--brand-blue) 0%, var(--brand-blue-light) 55%, var(--brand-blue) 100%);
    color: var(--card-white);
  }
  .back-mark {
    position: absolute; left: 0; right: 0; top: 128px;
    display: flex; align-items: center; justify-content: center; gap: 16px;
  }
  .back-mark .mark-square {
    width: 30px; height: 30px; background: var(--card-white);
  }
  .back-mark .mark-name {
    font-size: 40px; font-weight: 600; letter-spacing: 2px; color: var(--card-white);
  }
  .services {
    position: absolute; left: 0; right: 0; top: 303px;
    text-align: center; font-size: 13px; font-weight: 500; line-height: 20px;
  }
  .services .divider { color: rgba(255,255,255,0.5); margin: 0 5px; }

  /* Front side */
  .card-front { top: 521px; background: var(--card-white); }
  .front-mark {
    position: absolute; left: 26px; top: 46px;
    display: flex; align-items: center; gap: 14px;
  }
  .front-mark .mark-square { width: 26px; height: 26px; background: var(--brand-blue); }
  .front-mark .mark-name {
    font-size: 32px; font-weight: 600; color: var(--brand-blue); letter-spacing: 1px;
  }
  .person { position: absolute; left: 119px; top: 144px; }
  .person-name { font-size: 19px; font-weight: 700; color: var(--brand-blue); line-height: 24px; }
  .person-title { font-size: 15px; color: var(--text-grey); line-height: 20px; }
  .contacts { position: absolute; left: 117px; top: 199px; list-style: none; }
  .contacts li {
    display: flex; align-items: center; gap: 6px;
    font-size: 15px; color: var(--text-grey); line-height: 19.5px;
  }
  .contacts svg { width: 12px; height: 12px; fill: var(--brand-blue); }
  .address {
    position: absolute; left: 116px; top: 270px;
    font-size: 15px; color: var(--text-grey); line-height: 19.5px;
  }
  .band-grey-left {
    position: absolute; left: 0; top: 352px; width: 428px; height: 11px; background: var(--band-grey);
  }
  .band-grey-right {
    position: absolute; left: 624px; top: 352px; width: 37px; height: 11px; background: var(--band-grey);
  }
  .web {
    position: absolute; left: 439px; top: 346px;
    font-size: 15px; color: var(--text-grey);
  }
  .band-blue {
    position: absolute; left: 0; top: 369px; width: 661px; height: 8px; background: var(--brand-blue);
  }
</style>
</head>
<body>
  <section class="card card-back">
    <div class="back-mark">
      <span class="mark-square"></span>
      <span class="mark-name">MORVANE TALLY</span>
    </div>
    <p class="services">
      Cryptocurrency Exchange Services<span class="divider">|</span>Cryptocurrency Mining Operations<br>
      Cryptocurrency Investment Fund Offering
    </p>
  </section>

  <section class="card card-front">
    <div class="front-mark">
      <span class="mark-square"></span>
      <span class="mark-name">MORVANE TALLY</span>
    </div>
    <div class="person">
      <p class="person-name">Derek Wallis</p>
      <p class="person-title">Chief Operations Officer</p>
    </div>
    <ul class="contacts">
      <li>
        <svg viewBox="0 0 12 12"><path d="M2.5 0.5 L4.5 2.8 L3.4 4.2 C4 5.6 6 7.8 7.6 8.6 L9 7.5 L11.5 9.5 L10 11.5 C5 11 1 6.5 0.5 2 Z"/></svg>
        02 7153 2819
      </li>
      <li>
        <svg viewBox="0 0 12 12"><path d="M3 0 H9 V12 H3 Z M4 1.2 V9.5 H8 V1.2 Z M5.5 10.2 H6.5 V11.2 H5.5 Z" fill-rule="evenodd"/></svg>
        0418 395 207
      </li>
      <li>
        <svg viewBox="0 0 12 12"><path d="M0.5 2.5 H11.5 V9.5 H0.5 Z M1.5 3.3 L6 6.5 L10.5 3.3" fill-rule="evenodd"/><path d="M1.2 3.2 L6 6.6 L10.8 3.2" stroke="#fff" stroke-width="0.9" fill="none"/></svg>
        derek@morvanetally,com
      </li>
    </ul>
    <p class="address">
      Level 22, Halden Court, 48 Wirrapool St<br>
      Sydney NSW 2000<br>
      ABN : 57 304 918 226
    </p>
    <div class="band-grey-left"></div>
    <span class="web">www.morvanetally,com</span>
    <div class="band-grey-right"></div>
    <div class="band-blue"></div>
  </section>
</body>
</html>
```